Ridgefield High School Hockey Sponsorship Brochure

We our a high school hockey club based in the Chicago area in need of a 8.5 x 11 sponsorship brochure. I have copy and pictures, need layout design. Brochure will consist of Cover, 4 pages . Would like the font on the front cover to be the same as our website font. www.ridgefieldhshockey-example.com. On this inside cover I would like pictures of the flyers, players and crowd photo. Page 2 and 3 would be copy from the attached sponsorship package . Page 4 just include the Golf Sponsorship & Donations attachment. Back cover can be blank with Ridgefield web address. Use some or all attached pictures.

```html
<!DOCTYPE html>
<html lang="en">
<head>
<meta charset="utf-8">
<title>Stick &amp; Putts Golf Outing – Ridgefield High School Hockey Club</title>
<link rel="stylesheet" href="https://fonts.googleapis.com/css2?family=Playfair+Display:wght@700&family=Raleway:wght@400;500;600;700&display=swap">
<style>
:root{
  --purple:#5b2a86;
  --purple-deep:#3a1e52;
  --ink:#222226;
  --charcoal:#333338;
  --panel:#f1f1f2;
  --white:#ffffff;
  --body:'Raleway', Arial, sans-serif;
  --display:'Playfair Display', Georgia, serif;
}
*{margin:0;padding:0;box-sizing:border-box}
html,body{width:1200px;height:464px;overflow:hidden;background:#fff}
.brochure{position:relative;width:1200px;height:464px;overflow:hidden;font-family:var(--body);color:var(--ink)}
.spread-left{position:absolute;left:0;top:0;width:600px;height:464px;background:#fff}
.header-panel{position:absolute;left:0;top:0;width:288px;height:168px;
  background:radial-gradient(circle at 40% 75%,#5a2e86 0%,#2a1840 45%,#0d0b12 80%);}
.club-mark{position:absolute;left:46px;top:62px;display:flex;align-items:center;gap:8px}
.club-mark .mark-shape{width:38px;height:38px;border-radius:50%;background:#c9c9cf}
.club-mark .club-name{font-family:var(--body);font-weight:700;font-size:30px;color:#e6e6ea;line-height:1}
.club-mark .club-sub{font-family:var(--body);font-weight:700;font-size:8.5px;color:#e6e6ea;letter-spacing:.3px;margin-top:4px}
.intro{position:absolute;left:288px;top:0;width:312px;height:168px;background:var(--panel)}
.event-title{position:absolute;left:12px;top:24px;font-family:var(--display);font-size:26px;color:var(--purple);line-height:1}
.event-sub{position:absolute;left:12px;top:52px;font-family:var(--display);font-size:17px;color:var(--ink);line-height:1}
.title-rule{position:absolute;left:12px;top:79px;width:300px;height:5px}
.about-head{position:absolute;left:12px;top:91px;font-weight:700;font-size:8.5px;color:var(--purple)}
.about-copy{position:absolute;left:12px;top:101px;width:292px;font-size:6.7px;line-height:8.6px}
.about-copy p+p{margin-top:4px}
.tier-pill{position:absolute;height:16px;border-radius:0 8px 8px 0;color:#fff;font-size:8.6px;font-weight:500;padding:2px 0 0 14px}
.tier-pill b{font-weight:700}
.tier-pill.purple{background:var(--purple)}
.tier-pill.dark{background:var(--charcoal)}
.tier-list{position:absolute;font-size:6.8px;line-height:10px;list-style:none}
.tier-list li::before{content:"•";margin-right:4px}
.tier-note{position:absolute;font-size:6.8px;line-height:10px}
.feather-flag{position:absolute;left:288px;top:186px;width:26px;height:134px;background:linear-gradient(180deg,#1b2a22,#0e1612);border-radius:14px 2px 2px 2px}
.flag-base{position:absolute;left:284px;top:318px;width:18px;height:6px;border-radius:50%;background:#2d5a2a}
.hole-signs{position:absolute;left:340px;top:334px;display:flex;gap:5px}
.hole-signs span{width:32px;height:32px;border-radius:50%;background:radial-gradient(circle at 40% 35%,#f4f4f4,#bdbdbd)}
.raffle-band{position:absolute;left:0;top:392px;width:376px;height:52px;background:var(--purple-deep);border-radius:0 26px 26px 0}
.raffle-info{position:absolute;left:28px;top:6px;width:210px;color:#fff;font-size:6.9px;line-height:9px}
.raffle-info h3{font-size:8.6px;font-weight:700;margin-bottom:2px}
.contact-box{position:absolute;left:240px;top:0;width:136px;height:52px;background:#2a2a2e;border-radius:0 26px 26px 0;color:#fff;font-size:6.3px;line-height:9.5px;padding:6px 0 0 14px}
.contact-box strong{font-weight:700}
.site-url{position:absolute;left:398px;top:408px;font-size:12.6px;font-weight:500;color:var(--ink)}
.spread-right{position:absolute;left:600px;top:0;width:600px;height:464px}
.team-photo{position:absolute;inset:0;background:linear-gradient(135deg,#cfd4d8 0%,#8c9097 40%,#e4e7ea 65%,#5c5f66 100%)}
.frame{position:absolute;left:0;top:0}
.crest-name{position:absolute;left:812px;top:172px;width:172px;text-align:center;font-family:var(--body);font-weight:700;font-size:26px;color:#fff}
.crest-shape{position:absolute;left:862px;top:208px;width:72px;height:72px;background:#b9b9be}
</style>
</head>
<body>
<main class="brochure">
  <section class="spread-left">
    <div class="header-panel" role="img" aria-label="Purple halftone dot background">
      <div class="club-mark">
        <span class="mark-shape"></span>
        <div>
          <div class="club-name">Ridgefield</div>
          <div class="club-sub">HIGH SCHOOL HOCKEY CLUB</div>
        </div>
      </div>
    </div>

    <div class="intro">
      <h1 class="event-title">Stick &amp; Putts</h1>
      <h2 class="event-sub">Golf Outing</h2>
      <svg class="title-rule" viewBox="0 0 300 5" aria-hidden="true">
        <g fill="#5b2a86">
          <polygon points="0,0 16,0 13,5 0,5"/>
          <polygon points="19,0 33,0 30,5 16,5"/>
          <polygon points="36,0 50,0 47,5 33,5"/>
          <polygon points="53,0 67,0 64,5 50,5"/>
          <polygon points="70,0 84,0 81,5 67,5"/>
          <rect x="84" y="2" width="216" height="2"/>
        </g>
      </svg>
      <h3 class="about-head">About Us</h3>
      <div class="about-copy">
        <p>Ridgefield High School Hockey Club is a volunteered based, non for profit hockey club comprised of student athletes from Northbrook, Millbrook, Cedar Lake, Oak Ridge and Westfield High Schools. The Ridgefield mission is dedicated to the athletic development, personal growth and sportsmanship of High School hockey players.</p>
        <p>If you are a individual, family or company interested in giving back to the community and/or gaining exposure to a group of loyal families, we have many options to donate.</p>
      </div>
    </div>

    <div class="tier-pill purple" style="left:14px;top:180px;width:184px">Presenting Sponsor <b>$1000</b></div>
    <ul class="tier-list" style="left:20px;top:199px;width:270px">
      <li>Name on all printed promotional material - posters and signage</li>
      <li>Email blasts welcoming your business as a Presenting Sponsor</li>
      <li>Logo on website with link</li>
      <li>Email blast with special offer to families</li>
      <li>Complimentary foursome includes in 18 holes of golf, cart and lunch.</li>
      <li>Logo on social media sights</li>
      <li>Public acknowledgement at lunch</li>
      <li>Category exclusivity</li>
    </ul>

    <div class="tier-pill dark" style="left:14px;top:292px;width:184px">Contest Sponsor <b>$200</b></div>
    <p class="tier-note" style="left:14px;top:311px;width:280px">Support one of our contest Longest Drive, Longest Putt or Closest to the Pin.</p>
    <ul class="tier-list" style="left:20px;top:321px;width:270px">
      <li>Sign at the hole.</li>
      <li>Public acknowledgement at lunch.</li>
      <li>Company listing on Ridgefield website.</li>
    </ul>

    <div class="feather-flag" role="img" aria-label="Feather flag with club name"></div>
    <div class="flag-base"></div>

    <div class="tier-pill purple" style="left:328px;top:180px;width:182px">Driving Range Sponsor <b>$400</b></div>
    <ul class="tier-list" style="left:340px;top:199px;width:260px">
      <li>1 7' feather flag with company logo placed at driving range.</li>
      <li>Company listing on Ridgefield website.</li>
      <li>The feather flag sign is companies to keep after outing is completed.</li>
    </ul>

    <div class="tier-pill dark" style="left:328px;top:238px;width:182px">Beverage and Golf Cart Sponsor <b>$200</b></div>
    <ul class="tier-list" style="left:340px;top:258px;width:260px">
      <li>Signage with company logo on golf and beverage carts.</li>
      <li>Company listing on Ridgefield website</li>
    </ul>

    <div class="tier-pill purple" style="left:328px;top:292px;width:182px">Hole Sponsor <b>$100</b></div>
    <ul class="tier-list" style="left:340px;top:311px;width:260px">
      <li>Signage with company logo at hole.</li>
      <li>Company listing on Ridgefield website.</li>
    </ul>

    <div class="hole-signs" role="img" aria-label="Golf ball hole signs with sponsor names">
      <span></span><span></span><span></span><span></span><span></span>
    </div>

    <div class="raffle-band">
      <div class="raffle-info">
        <h3>Raffle Donations</h3>
        <p>We are accepting donations for our silent auction and raffle.<br>Donors receive a listing on Ridgefield website.<br>www.ridgefieldhshockey-example.com</p>
      </div>
      <div class="contact-box">
        <strong>Dan Keller</strong><br>
        Director of Marketing<br>
        dan.keller@ridgefieldhshockey-example.com<br>
        555 010 4821
      </div>
    </div>

    <p class="site-url">www.ridgefieldhshockey-example.com</p>
  </section>

  <section class="spread-right">
    <div class="team-photo" role="img" aria-label="Collage of hockey players celebrating, skating and a goalie making a save"></div>
    <svg class="frame" width="600" height="464" viewBox="0 0 600 464" aria-hidden="true">
      <defs>
        <linearGradient id="frameGrad" x1="0" y1="0" x2="0" y2="1">
          <stop offset="0" stop-color="#5b2a86"/>
          <stop offset="1" stop-color="#111"/>
        </linearGradient>
      </defs>
      <rect x="18" y="30" width="546" height="406" fill="none" stroke="url(#frameGrad)" stroke-width="6"/>
      <rect x="30" y="40" width="526" height="384" fill="none" stroke="#111" stroke-width="5"/>
      <polygon points="298,100 412,166 412,297 298,363 184,297 184,166" fill="#0b0b0d" stroke="#fff" stroke-width="3"/>
    </svg>
    <div class="crest-name" style="left:212px">Ridgefield</div>
    <div class="crest-shape" style="left:262px"></div>
  </section>
</main>
</body>
</html>
```